Brantley Studios photography and video creator

I need a business card for my production company. I shoot photography and videography for real estate, adventure sports and businesses

Contact Information for Business Card

simple not to busy

Colors

Designer to choose colors to be used in the design.

Requirements
Must have
• derek@brantleystudios.ca
• phone -5873304127
• instagram derek_brantley

```html
<!DOCTYPE html>
<html lang="en">
<head>
<meta charset="utf-8">
<title>Brantley Studios — Business Card</title>
<link href="https://fonts.googleapis.com/css2?family=Montserrat:wght@500;700&display=swap" rel="stylesheet">
<style>
  :root {
    --backdrop: #dedede;
    --ink: #1e1e1e;
    --ink-deep: #0c0c0c;
    --mist: #f2f2f2;
    --fog: #a9a9a9;
    --slate: #6f6f6f;
    --paper: #f5f5f5;
    --white: #ffffff;
  }
  * { margin: 0; padding: 0; box-sizing: border-box; }
  html, body {
    width: 1200px;
    height: 1200px;
    overflow: hidden;
    background: var(--backdrop);
    font-family: "Montserrat", sans-serif;
  }
  .canvas { position: relative; width: 1200px; height: 1200px; }

  .card {
    position: absolute;
    left: 220px;
    width: 758px;
    height: 433px;
    overflow: hidden;
  }
  .card--front { top: 109px; }
  .card--back { top: 648px; background: var(--paper); }

  .landscape {
    position: absolute;
    inset: 0;
    background: linear-gradient(180deg,
      var(--mist) 0%,
      var(--fog) 28%,
      var(--slate) 48%,
      var(--ink) 70%,
      var(--ink-deep) 100%);
  }

  .brand {
    position: absolute;
    left: 0;
    right: 0;
    display: flex;
    align-items: center;
    justify-content: center;
    gap: 14px;
  }
  .brand__dot {
    width: 22px;
    height: 22px;
    border-radius: 50%;
  }
  .brand__name {
    font-weight: 700;
    font-size: 36px;
    letter-spacing: 0.5px;
    text-transform: uppercase;
  }
  .card--front .brand { top: 256px; }
  .card--front .brand__dot { background: var(--white); }
  .card--front .brand__name { color: var(--white); }
  .card--back .brand { top: 190px; }
  .card--back .brand__dot { background: var(--ink); }
  .card--back .brand__name { color: var(--ink); }

  .contact {
    position: absolute;
    display: flex;
    align-items: center;
    gap: 16px;
    color: var(--white);
  }
  .contact svg { width: 28px; height: 28px; flex: none; }
  .contact--phone { left: 30px; top: 350px; }
  .contact--phone .contact__text { font-weight: 700; font-size: 19px; letter-spacing: 0.5px; }
  .contact--email { left: 30px; top: 385px; }
  .contact--email .contact__text { font-weight: 500; font-size: 17px; }
  .contact--social { right: 26px; top: 385px; }
  .contact--social .contact__text { font-weight: 500; font-size: 17px; }
</style>
</head>
<body>
<main class="canvas">

  <section class="card card--front">
    <div class="landscape" role="img" aria-label="Soft misty mountain ranges with tall evergreen trees in shades of grey"></div>

    <div class="brand">
      <span class="brand__dot"></span>
      <span class="brand__name">Brantley Studios</span>
    </div>

    <div class="contact contact--phone">
      <svg viewBox="0 0 28 28" aria-hidden="true">
        <path d="M7 3 L11 3 L13 9 L10 11 C11.5 14.5 13.5 16.5 17 18 L19 15 L25 17 L25 21 C25 23 23 25 21 25 C12 24 4 16 3 7 C3 5 5 3 7 3 Z" fill="none" stroke="#ffffff" stroke-width="2" stroke-linejoin="round"/>
        <path d="M17 3 A8 8 0 0 1 25 11 M17 7 A4 4 0 0 1 21 11" fill="none" stroke="#ffffff" stroke-width="1.6" stroke-linecap="round"/>
      </svg>
      <span class="contact__text">5873304127</span>
    </div>

    <div class="contact contact--email">
      <svg viewBox="0 0 28 28" aria-hidden="true">
        <rect x="1" y="5" width="26" height="18" fill="#ffffff"/>
        <path d="M1 5 L14 16 L27 5 M1 23 L11 13.5 M27 23 L17 13.5" fill="none" stroke="#1e1e1e" stroke-width="1.6"/>
      </svg>
      <span class="contact__text">derek@brantleystudios.ca</span>
    </div>

    <div class="contact contact--social">
      <span class="contact__text">derek_brantley</span>
    </div>
  </section>

  <section class="card card--back">
    <div class="brand">
      <span class="brand__dot"></span>
      <span class="brand__name">Brantley Studios</span>
    </div>
  </section>

</main>
</body>
</html>
```